Brantmoor Financial Coaching LLC - Needed clean black business card

Business card for personal financial coaching practice located on Las Vegas NV, new startup. Back of card needs to have "how it works" to match the website.

Font styles to use
Sans Serif

Colors

Designer to choose colors to be used in the design.

```html
<!DOCTYPE html>
<html lang="en">
<head>
<meta charset="utf-8">
<title>Brantmoor Financial Coaching LLC – Business Card</title>
<link href="https://fonts.googleapis.com/css2?family=Montserrat:wght@500;600&family=Roboto:wght@400&display=swap" rel="stylesheet">
<style>
  :root {
    --backdrop: #e6e3df;
    --card: #060808;
    --accent: #27a4dc;
    --text: #e2e2e2;
    --heading-font: "Montserrat", sans-serif;
    --body-font: "Roboto", sans-serif;
  }
  * { margin: 0; padding: 0; box-sizing: border-box; }
  html, body {
    width: 1111px;
    height: 1200px;
    overflow: hidden;
    background: var(--backdrop);
  }
  .card {
    position: absolute;
    left: 202px;
    width: 726px;
    height: 404px;
    background: var(--card);
  }
  .card--front { top: 142px; }
  .card--back { top: 631px; }

  .company-name {
    position: absolute;
    font-family: var(--heading-font);
    font-weight: 500;
    font-size: 33px;
    color: var(--accent);
    white-space: nowrap;
    line-height: 1;
  }
  .card--front .company-name { left: 61px; top: 60px; }
  .card--back .company-name { left: 0; right: 0; text-align: center; top: 80px; }

  .person-name {
    position: absolute;
    left: 61px;
    top: 198px;
    font-family: var(--heading-font);
    font-weight: 500;
    font-size: 26px;
    color: var(--accent);
    line-height: 1;
  }
  .contact-list {
    position: absolute;
    left: 61px;
    top: 240px;
    list-style: none;
    font-family: var(--body-font);
    font-size: 18px;
    line-height: 24px;
    color: var(--text);
  }
  .contact-label { color: var(--accent); }
  .divider {
    position: absolute;
    left: 61px;
    top: 318px;
    width: 593px;
    height: 2px;
    background: var(--accent);
  }
  .address {
    position: absolute;
    left: 61px;
    top: 328px;
    font-family: var(--body-font);
    font-size: 18px;
    line-height: 24px;
    color: var(--text);
  }

  .section-title {
    position: absolute;
    left: 0; right: 0;
    top: 201px;
    text-align: center;
    font-family: var(--heading-font);
    font-weight: 500;
    font-size: 26px;
    color: var(--accent);
    line-height: 1;
  }
  .section-copy {
    position: absolute;
    left: 43px;
    width: 637px;
    top: 242px;
    font-family: var(--body-font);
    font-size: 17.5px;
    line-height: 25px;
    color: var(--text);
    text-align: justify;
    text-align-last: center;
    hyphens: auto;
  }
</style>
</head>
<body>
  <section class="card card--front">
    <h1 class="company-name">Brantmoor Financial Coaching LLC</h1>
    <h2 class="person-name">Marcus Brantmoor</h2>
    <ul class="contact-list">
      <li><span class="contact-label">P :</span> 702-555-0148</li>
      <li><span class="contact-label">E :</span> Marcus@brantmoorfinancialcoaching.com</li>
      <li><span class="contact-label">W :</span> brantmoorfinancialcoaching.com</li>
    </ul>
    <div class="divider"></div>
    <p class="address"><span class="contact-label">A :</span> 4120 W Sahara Ave #305-B Las Vegas, NV 89102</p>
  </section>

  <section class="card card--back">
    <h1 class="company-name">Brantmoor Financial Coaching LLC</h1>
    <h2 class="section-title">How It Works</h2>
    <p class="section-copy">All free one-time consultations are in-person meetings only. Paid appointments may be scheduled for in-person or virtual meetings. Select the session, date and time that works best for your schedule. Start your journey of financial freedom at brantmoorfinancialcoaching.com</p>
  </section>
</body>
</html>
```